New Business Cards for Organic Meat Farm

We need a business card designed for Quenwick Farm, a meat farm in western MA. Our logo uses a hand-drawn woodcut (attached). Our color palette has been simply black and white (shown in notepad and picture of our food truck). While we are based out of western MA, we have ambitions to grow nationally, so our hope is for a classy and memorable card which will be printed on a premium quality stock from a printer like printkestrel.com.
Target Market(s)
consumers of quality meats, restauranteurs, partnering farms
Industry/Entity Type
Farming and prepared meat products
Contact Information for Business Card
Wendell Pruitt, President/Owner, wendell@quenwickfarm.com, mobile: 413-555-0172, phone: 413-555-0148, quenwickfarm.com, facebook: @quenwickfarm, instagram: @thornburyfarmma
Colors
Designer to choose colors to be used in the design.
Look and feel

```html
<!DOCTYPE html>
<html lang="en">
<head>
<meta charset="utf-8">
<title>Quenwick Farm – Business Card</title>
<link href="https://fonts.googleapis.com/css2?family=Montserrat:wght@400;500;700&display=swap" rel="stylesheet">
<style>
  :root {
    --backdrop: #cfd4d4;
    --stock: #efefed;
    --ink: #111111;
    --ink-soft: #4a4a4a;
    --edge: #0b0b0b;
  }
  * { margin: 0; padding: 0; box-sizing: border-box; }
  html, body { width: 1200px; height: 881px; overflow: hidden; }
  body {
    background: var(--backdrop);
    font-family: "Montserrat", Arial, sans-serif;
    color: var(--ink);
    display: flex;
    flex-direction: column;
    align-items: center;
    justify-content: center;
    gap: 48px;
  }
  .card {
    width: 616px;
    height: 352px;
    background: var(--stock);
    border-bottom: 4px solid var(--edge);
    position: relative;
  }
  .brand-mark {
    display: flex;
    flex-direction: column;
    align-items: center;
    gap: 14px;
  }
  .brand-art {
    width: 200px;
    height: 96px;
    border-radius: 100px 100px 8px 8px;
    background: linear-gradient(180deg, #3a3a3a, #777 60%, #bdbdbd);
  }
  .brand-name {
    font-weight: 700;
    font-size: 30px;
    letter-spacing: 0.5px;
    color: var(--ink);
    white-space: nowrap;
  }
  /* Contact side */
  .card-contact { display: flex; align-items: center; }
  .card-contact .brand-mark { width: 300px; }
  .card-contact .brand-name { font-size: 26px; }
  .divider {
    width: 1.5px;
    height: 250px;
    background: var(--ink);
  }
  .contact-block { padding-left: 28px; }
  .person-name { font-weight: 700; font-size: 26px; line-height: 1.1; }
  .person-title { font-size: 15px; color: var(--ink-soft); margin: 4px 0 14px; }
  .contact-list { list-style: none; }
  .contact-list li {
    display: flex;
    align-items: center;
    gap: 10px;
    font-size: 15px;
    line-height: 1.6;
    white-space: nowrap;
  }
  .contact-list svg { width: 13px; height: 13px; flex: none; }
  /* Logo side */
  .card-logo { display: flex; align-items: center; justify-content: center; }
  .card-logo .brand-art { width: 240px; height: 116px; }
</style>
</head>
<body>

  <section class="card card-contact">
    <div class="brand-mark">
      <div class="brand-art" role="img" aria-label="Woodcut illustration of the farmhouse with trees"></div>
      <span class="brand-name">Quenwick Farm</span>
    </div>
    <div class="divider"></div>
    <div class="contact-block">
      <h1 class="person-name">Wendell Pruitt</h1>
      <p class="person-title">President/Owner</p>
      <ul class="contact-list">
        <li><svg viewBox="0 0 12 12"><rect x="3" y="0.5" width="6" height="11" rx="1" fill="none" stroke="currentColor"/></svg>413-555-0172</li>
        <li><svg viewBox="0 0 12 12"><path d="M2 1l2.5 0 1 3-1.5 1c.7 1.5 1.5 2.3 3 3l1-1.5 3 1v2.5c-5 .5-9.5-4-9-9z" fill="currentColor"/></svg>413-555-0148</li>
        <li><svg viewBox="0 0 12 12"><rect x="0.5" y="2" width="11" height="8" fill="currentColor"/><path d="M0.5 2l5.5 4.5 5.5-4.5" fill="none" stroke="#efefed"/></svg>wendell@quenwickfarm.com</li>
        <li><svg viewBox="0 0 12 12"><circle cx="6" cy="6" r="5.5" fill="currentColor"/><path d="M.5 6h11M6 .5c-2.5 3-2.5 8 0 11M6 .5c2.5 3 2.5 8 0 11" fill="none" stroke="#efefed" stroke-width=".8"/></svg>quenwickfarm.com</li>
        <li><svg viewBox="0 0 12 12"><circle cx="6" cy="6" r="5.5" fill="currentColor"/></svg>@quenwickfarm</li>
        <li><svg viewBox="0 0 12 12"><rect x="0.5" y="0.5" width="11" height="11" rx="3" fill="none" stroke="currentColor"/></svg>@quenwickfarm</li>
      </ul>
    </div>
  </section>

  <section class="card card-logo">
    <div class="brand-mark">
      <div class="brand-art" role="img" aria-label="Woodcut illustration of the farmhouse with trees"></div>
      <span class="brand-name">Quenwick Farm</span>
    </div>
  </section>

</body>
</html>
```